practical mindfulness guide needs a book cover, back and front

I require a book cover for a print and eBook. Both front and back. The title of the book is: Returning Toward Stillness:
Restoring Your Routine to Ease Worry, Grow Inner Steadiness, and Open Your Boundless Capacity.
Sales Handle
Eight weeks is good, fifty-two is better: this warm, personal guide will help you deepen in mindfulness across the year, weaving it into all aspects of your life.

Back cover
Returning Toward Stillness offers an evidence-based, step-by-step journey through a year of personal change. Drawing on his path of overcoming dyslexia, autism, trauma, and anxiety, Dr. Marcus Tolland blends mindfulness, psychology, and holistic healing in this accessible guide to lasting personal transformation.

Unlike short-term programs, this book offers a full year of structured, practical exercises—scientifically grounded and deeply personal—to help you turn mindfulness into a lifelong habit. Each week, you'll explore simple yet profound practices to manage stress, build emotional resilience, and reconnect with your deeper wisdom. Through guided meditations, reflections, and trainings, you’ll rewire old patterns and learn to embrace the present moment with clarity and compassion. Whether you're seeking relief from chronic stress, clarity in uncertain times, or a deeper connection to yourself and your life, Quiet Awakening will meet you where you are. It’s not about perfection—it’s about learning to show up, fully present, for the beauty and messiness of life.

Bio
Marcus Tolland is a mindfulness and Dharma teacher, award-winning author, and former professor of social work with over 40 years of contemplative practice. He teaches insight meditation and has worked extensively with diverse communities, including unhoused populations, combat veterans with PTSD, and First Nations groups, blending mindfulness with deep cultural respect. Marcus holds a PhD in social work and has authored several mindfulness and social justice books. He teaches with Clear Meadow Sangha (CMS) and founded the Pinegate Silent Sitting Circle. His teaching invites a return to presence, clarity, and compassionate action.

I like the simple design of the book Stillness: The Surprising Story Beneath Contemplation and Living Awake in Each Day. But something more eye-catching would be welcome. It is a book for someone who has taken an intro mindfulness course and wants to get back into it, hence the "coming back" in the title. AI suggested things like a calendar with "practice" written on one day, with it crossed out. At any rate, it would be nice to illustrate this idea of coming back or renewing mindfulness practice with a 52-week practice guide. The book is basically 52 topics with an intro, reflections, practices, and encouragement.

Target Market(s)

Someone who has completed a short introductory mindfulness program like MBSR or MBCT and aims to cultivate a consistent, sustainable meditation and mindfulness practice. Eight weeks is a great start, but it simply isn’t enough time to firmly establish the habits of mindfulness, much less to delve into the layers of somatic and emotional nuance that it can offer. People require varying support levels. For example, those with chronic depression may need intensive follow-ups, while others might benefit from occasional refreshers. This book offers a flexible approach that readers can tailor to their own needs. The secondary target audience includes individuals who had a previous meditation practice but have let it lapse and wish to revitalize it. Through positive reviews, press, social media, and word-of-mouth, I also hope to attract other types of readers, such as those experiencing high stress or anxiety, individuals navigating major life transitions, professionals like therapists, counselors, and coaches, people seeking to develop resiliency or emotional intelligence, and those curious about integrating spiritual wisdom into everyday life.

Industry/Entity Type

Self help

Colors
0054AA
0677BA
7BADD7
CADEEF
E8F1F8

Requirements
Must have
• The title and my name as Marcus J. Tolland. Provided logo on bottom of back cover
Nice to have
• Something that says this book is for those coming back to practice. some tie in with my Vidora channel at https://www.vidora-example.net/@marcusquietmind
Should not have
• Buddhas or other religious symbols

```html
<!DOCTYPE html>
<html lang="en">
<head>
<meta charset="utf-8">
<title>Returning Toward Stillness — Cover</title>
<link href="https://fonts.googleapis.com/css2?family=Gloock&family=Barlow:wght@500;600&display=swap" rel="stylesheet">
<style>
  :root {
    --stage: #1b1b1b;
    --navy: #0054aa;
    --ocean: #0677ba;
    --sky: #7badd7;
    --mist: #cadeef;
    --haze: #e8f1f8;
    --white: #ffffff;
    --ink: #111111;
    --water: #bfeefa;
  }
  * { margin: 0; padding: 0; box-sizing: border-box; }
  html, body { width: 1200px; height: 1029px; overflow: hidden; background: var(--stage); }
  .canvas { position: relative; width: 1200px; height: 1029px; }

  .serif { font-family: "Gloock", Georgia, serif; }
  .sans { font-family: "Barlow", Arial, sans-serif; }

  /* Back cover */
  .back-cover {
    position: absolute; left: 45px; top: 218px; width: 377px; height: 592px;
    background: linear-gradient(180deg, var(--white) 0%, var(--white) 62%, var(--haze) 80%, var(--water) 100%);
    overflow: hidden;
  }
  .back-blurb, .back-bio {
    position: absolute; left: 45px; width: 315px;
    font-family: "Barlow", Arial, sans-serif; font-weight: 500;
    font-size: 8.3px; line-height: 16.5px; color: var(--ink); text-align: center;
  }
  .back-blurb { top: 40px; }
  .back-blurb p + p { margin-top: 0; }
  .bio-heading {
    position: absolute; left: 0; top: 305px; width: 123px; height: 21px;
    background: var(--navy); color: var(--white);
    font-family: "Barlow", Arial, sans-serif; font-weight: 600;
    font-size: 10px; letter-spacing: 1.6px; line-height: 21px; padding-left: 44px;
  }
  .back-bio { top: 332px; left: 50px; width: 310px; }
  .back-photo {
    position: absolute; left: 0; bottom: 0; width: 377px; height: 128px;
    background: linear-gradient(180deg, rgba(255,255,255,0) 0%, rgba(190,200,205,0.55) 30%, rgba(191,238,250,0.6) 60%, var(--water) 100%);
  }
  .publisher-mark {
    position: absolute; left: 0; width: 377px; bottom: 48px;
    display: flex; align-items: center; justify-content: center; gap: 6px;
    font-family: "Barlow", Arial, sans-serif; font-weight: 600; font-size: 11px;
    color: var(--navy); letter-spacing: 0.5px;
  }
  .publisher-mark .dot { width: 14px; height: 14px; border-radius: 50%; background: var(--navy); }

  /* Spine */
  .spine {
    position: absolute; left: 422px; top: 218px; width: 42px; height: 592px;
    background: var(--navy);
  }
  .spine-name {
    position: absolute; left: 42px; top: 196px; transform-origin: 0 0; transform: rotate(90deg);
    font-family: "Gloock", Georgia, serif; font-size: 24px; color: var(--white);
    white-space: nowrap; line-height: 42px; letter-spacing: 0.5px;
  }

  /* Front cover */
  .front-cover {
    position: absolute; left: 464px; top: 218px; width: 380px; height: 592px;
    background: linear-gradient(200deg, var(--sky) 0%, var(--mist) 25%, var(--white) 48%, var(--white) 100%);
    overflow: hidden;
  }
  .title { text-align: center; color: var(--navy); font-family: "Gloock", Georgia, serif; font-weight: 400; }
  .front-cover .title { position: absolute; top: 45px; left: 0; width: 380px; font-size: 36px; line-height: 42px; }
  .subtitle {
    text-align: center; color: var(--ink); text-transform: uppercase;
    font-family: "Barlow", Arial, sans-serif; font-weight: 500;
  }
  .front-cover .subtitle { position: absolute; top: 139px; left: 30px; width: 320px; font-size: 11.6px; line-height: 18px; letter-spacing: 1.7px; }
  .handle {
    position: absolute; left: 0; background: var(--navy); color: var(--white); text-align: center;
    font-family: "Barlow", Arial, sans-serif; font-weight: 500;
  }
  .front-cover .handle { top: 218px; width: 380px; height: 62px; padding: 6px 28px 0; font-size: 10px; line-height: 16.5px; }
  .cover-photo {
    position: absolute; left: 0; bottom: 0;
    background: linear-gradient(180deg, var(--sky) 0%, var(--mist) 35%, #8ea4bf 55%, var(--mist) 72%, var(--haze) 100%);
  }
  .front-cover .cover-photo { width: 380px; height: 312px; }
  .author {
    position: absolute; left: 0; text-align: center; color: var(--navy);
    font-family: "Gloock", Georgia, serif;
  }
  .front-cover .author { top: 504px; width: 380px; font-size: 35px; line-height: 40px; }

  /* eBook thumbnail */
  .ebook-cover {
    position: absolute; left: 907px; top: 282px; width: 248px; height: 438px;
    background: linear-gradient(200deg, var(--sky) 0%, var(--mist) 25%, var(--white) 48%, var(--white) 100%);
    overflow: hidden;
  }
  .ebook-cover .title { position: absolute; top: 22px; left: 0; width: 248px; font-size: 25px; line-height: 31px; }
  .ebook-cover .subtitle { position: absolute; top: 91px; left: 14px; width: 220px; font-size: 8.6px; line-height: 13px; letter-spacing: 1px; }
  .ebook-cover .handle { top: 153px; width: 248px; height: 47px; padding: 4px 8px 0; font-size: 7.2px; line-height: 12.4px; font-weight: 600; }
  .ebook-cover .cover-photo { width: 248px; height: 236px; }
  .ebook-cover .author { top: 384px; left: 8px; width: 248px; font-size: 25px; line-height: 30px; }
</style>
</head>
<body>
<div class="canvas">

  <section class="back-cover">
    <div class="back-blurb">
      <p>Returning Toward Stillness offers an evidence-based, step-by-step journey through a year of personal change. Drawing on his path of overcoming dyslexia, autism, trauma, and anxiety, Dr. Marcus Tolland blends mindfulness, psychology, and holistic healing in this accessible guide to lasting personal transformation.</p>
      <p>Unlike short-term programs, this book offers a full year of structured, practical exercises—scientifically grounded and deeply personal—to help you turn mindfulness into a lifelong habit. Each week, you'll explore simple yet profound practices to manage stress, build emotional resilience, and reconnect with your deeper wisdom. Through guided meditations, reflections, and trainings, you'll rewire old patterns and learn to embrace the present moment with clarity and compassion. Whether you're seeking relief from chronic stress, clarity in uncertain times, or a deeper connection to yourself and your life, Quiet Awakening will meet you where you are. It's not about perfection—it's about learning to show up, fully present, for the beauty and messiness of life.</p>
    </div>
    <div class="bio-heading">BIOGRAPHY</div>
    <div class="back-bio">
      <p>Marcus Tolland is a mindfulness and Dharma teacher, award-winning author, and former professor of social work with over 40 years of contemplative practice. He teaches insight meditation and has worked extensively with diverse communities, including unhoused populations, combat veterans with PTSD, and First Nations groups, blending mindfulness with deep cultural respect. Marcus holds a PhD in social work and has authored several mindfulness and social justice books. He teaches with Clear Meadow Sangha (CMS) and founded the Pinegate Silent Sitting Circle. His teaching invites a return to presence, clarity, and compassionate action.</p>
    </div>
    <div class="back-photo" role="img" aria-label="Smooth pale stones resting on calm, light blue water"></div>
    <div class="publisher-mark"><span class="dot"></span>Stillpoint Press</div>
  </section>

  <section class="spine">
    <div class="spine-name">Marcus J. Tolland</div>
  </section>

  <section class="front-cover">
    <h1 class="title">Returning Toward<br>Stillness</h1>
    <p class="subtitle">Restoring Your Routine to Ease Worry, Grow Inner Steadiness, and Open Your Boundless Capacity.</p>
    <p class="handle">Eight weeks is good, fifty-two is better: this warm, personal guide will help you deepen in mindfulness across the year, weaving it into all aspects of your life.</p>
    <div class="cover-photo" role="img" aria-label="An arch of balanced blue-grey stones rising from still water under a bright sky"></div>
    <p class="author">Marcus J. Tolland</p>
  </section>

  <section class="ebook-cover">
    <h2 class="title">Returning Toward<br>Stillness</h2>
    <p class="subtitle">Restoring Your Routine to Ease Worry, Grow Inner Steadiness, and Open Your Boundless Capacity.</p>
    <p class="handle">Eight weeks is good, fifty-two is better: this warm, personal guide will help you deepen in mindfulness across the year, weaving it into all aspects of your life.</p>
    <div class="cover-photo" role="img" aria-label="An arch of balanced blue-grey stones rising from still water under a bright sky"></div>
    <p class="author">Marcus J. Tolland</p>
  </section>

</div>
</body>
</html>
```